Business card design for crowd sourced review site.

I need a business card magnet design for an online, crowd-sourced, restaurant review site strictly for Kosher restaurants.
It is similar to WanderNotes but catering to a very particular crowd.
The markets it will be distributed in are flooded with business card fridge magnets so this needs to be eye-catching and unique. The Business name is PlateRanker
The website isnt finished but you can see the basic setup here
http://dining.brevtalo.com/

The second image i included is another logo design I liked and was thinking about using and decided I will probably also make a SECOND custom cut business card in the shape of that icon. Bonus if you can throw that in also.

Target Market(s)

Jewish consumers aged 20-35

Industry/Entity Type

Business

Contact Information for Business Card

see description.
Design should not be too crowded and should in eye-catching. Will mainly be used as fridge magnets.

Requirements
Must have
• Website address. logo.
Nice to have
• tagline. (The Definitive guide to kosher dining for the Kosher consumer)
• Im not a professional but I personally think the color blue goes along with this concept. ill leave it to you to decide.
Should not have
• any religious symbols.

```html
<!DOCTYPE html>
<html lang="en">
<head>
<meta charset="utf-8">
<title>PlateRanker Business Card</title>
<link href="https://fonts.googleapis.com/css2?family=Open+Sans:ital,wght@0,400;0,600;1,400&display=swap" rel="stylesheet">
<style>
  :root {
    --bg: #e9e6e1;
    --card-black: #0d0d0d;
    --card-black-soft: #1c1c1c;
    --brand-red: #e1351f;
    --brand-red-dark: #b8281a;
    --text-light: #f2f2f2;
    --text-muted: #c9c9c9;
    --strip-white: #f4f4f4;
  }
  * { margin: 0; padding: 0; box-sizing: border-box; }
  html, body {
    width: 1200px; height: 950px; overflow: hidden;
    background: var(--bg);
    font-family: "Open Sans", Arial, sans-serif;
  }
  .card {
    position: absolute; left: 250px; width: 700px; height: 400px;
    border-radius: 4px; overflow: hidden;
    box-shadow: 0 10px 28px rgba(0,0,0,.25);
  }
  /* Front */
  .card-front {
    top: 50px;
    background: linear-gradient(135deg, var(--card-black-soft) 0%, var(--card-black) 55%);
    color: var(--text-light);
  }
  .edge-strip { position: absolute; right: 0; top: 0; width: 22px; height: 100%; }
  .edge-strip .strip-top { height: 52%; background: var(--strip-white); }
  .edge-strip .strip-bottom { height: 48%; background: var(--brand-red); }
  .divider {
    position: absolute; left: 390px; top: 40px; width: 1px; height: 320px;
    background: var(--brand-red-dark);
  }
  .brand {
    position: absolute; display: flex; align-items: center; gap: 12px;
    font-weight: 600; color: var(--text-light);
  }
  .front-brand { left: 60px; top: 70px; font-size: 38px; }
  .brand-dot { width: 18px; height: 18px; border-radius: 50%; background: var(--brand-red); flex: none; }
  .person { position: absolute; left: 60px; bottom: 70px; }
  .person-name { font-size: 26px; color: var(--brand-red); }
  .person-role { font-size: 19px; color: var(--text-light); margin-top: 2px; }
  .address {
    position: absolute; left: 420px; top: 60px;
    font-size: 18px; line-height: 1.55; color: var(--text-light);
  }
  .contact { position: absolute; left: 420px; bottom: 48px; list-style: none; }
  .contact li {
    display: flex; align-items: center; gap: 12px;
    font-size: 18px; line-height: 1.6; color: var(--text-muted);
  }
  .contact svg { width: 16px; height: 16px; fill: var(--brand-red); flex: none; }
  /* Back */
  .card-back {
    top: 500px;
    background: var(--brand-red);
    color: #fff;
    display: flex; flex-direction: column; align-items: center; justify-content: center;
  }
  .back-brand { position: static; font-size: 64px; color: #fff; }
  .back-brand .brand-dot { background: #fff; width: 26px; height: 26px; }
  .tagline { margin-top: 18px; font-size: 18px; font-style: italic; color: #fff; }
</style>
</head>
<body>
  <section class="card card-front">
    <div class="brand front-brand"><span class="brand-dot"></span>PlateRanker</div>
    <div class="divider"></div>
    <div class="person">
      <p class="person-name">Daniel Roth</p>
      <p class="person-role">President</p>
    </div>
    <address class="address" style="font-style:normal">
      1420 Linden Avenue<br>
      Maple Grove, NY 11020<br>
      www.plateranker.com
    </address>
    <ul class="contact">
      <li><svg viewBox="0 0 16 16"><path d="M3 1h3l1.5 4-2 1.2a9 9 0 0 0 4.3 4.3L11 8.5l4 1.5v3a2 2 0 0 1-2 2A12 12 0 0 1 1 3a2 2 0 0 1 2-2z"/></svg>555 0147 2210</li>
      <li><svg viewBox="0 0 16 16"><path d="M4 1h8a1 1 0 0 1 1 1v12a1 1 0 0 1-1 1H4a1 1 0 0 1-1-1V2a1 1 0 0 1 1-1zm1 2v9h6V3z"/></svg>555 0183 6642</li>
      <li><svg viewBox="0 0 16 16"><path d="M2 5h12v9H2zM4 1h8v3H4zm1 7h6v4H5z"/></svg>555 0129 4475</li>
      <li><svg viewBox="0 0 16 16"><path d="M1 3h14v10H1zm1.5 1.5v.4L8 8.6l5.5-3.7v-.4z"/></svg>daniel@plateranker.com</li>
    </ul>
    <div class="edge-strip"><div class="strip-top"></div><div class="strip-bottom"></div></div>
  </section>

  <section class="card card-back">
    <div class="brand back-brand"><span class="brand-dot"></span>PlateRanker</div>
    <p class="tagline">a guide to kosher dining for the Kosher consumer</p>
  </section>
</body>
</html>
```